Business Card for a Floral & Decorating Business

I would like to take my current logo and create a better business card. I am looking for elegance as I am a florist and event decorator. My logo has multiple colour options. I like colours like green, purple, pink and orange, I think I would like a white card, open to black back ground. I want it to feel elegant and romantic. I like metallic lettering that maybe is indented in the paper, I also like glossy paper. I have a full logo already as well as a badge. I have attached both in multiple colours.m
Updates

Need extra days to review

Target Market(s)

Weddings, special events, floral customers

Industry/Entity Type

Floral and decorating

Contact Information for Business Card

Phone number, email, instagram, facebook, title, name, logo

Font styles to use
Script

Requirements
Nice to have
• Elegant

```html
<!DOCTYPE html>
<html lang="en">
<head>
<meta charset="utf-8">
<title>Marlow Ashby – Business Card</title>
<link rel="stylesheet" href="https://fonts.googleapis.com/css2?family=Lato:wght@400;700&display=swap">
<style>
  :root {
    --backdrop: #e6e6e4;
    --wine: #96325c;
    --wine-deep: #7c2549;
    --paper: #ffffff;
    --blush: #f3dbe5;
  }
  * { box-sizing: border-box; margin: 0; padding: 0; }
  html, body { width: 1200px; height: 802px; overflow: hidden; }
  body {
    background: var(--backdrop);
    font-family: "Lato", Arial, sans-serif;
    display: flex;
    align-items: center;
    justify-content: center;
    gap: 40px;
  }
  .card {
    position: relative;
    width: 540px;
    height: 309px;
    background: var(--wine);
    color: var(--paper);
    overflow: hidden;
    box-shadow: 0 8px 20px rgba(0,0,0,0.12);
  }

  /* Contact side */
  .floral-monogram {
    position: absolute;
    left: 0; top: 0;
    width: 215px; height: 100%;
    background: linear-gradient(135deg, var(--paper) 0%, var(--blush) 100%);
  }
  .contact-side .brand {
    position: absolute;
    left: 250px; top: 44px;
    display: flex; align-items: center; gap: 8px;
  }
  .brand-mark {
    width: 10px; height: 10px; border-radius: 50%;
    background: var(--paper);
  }
  .brand-name {
    font-weight: 400;
    font-size: 26px;
    letter-spacing: 0.5px;
    color: var(--paper);
  }
  .person {
    position: absolute;
    left: 250px; top: 112px;
  }
  .person-name {
    font-weight: 700;
    font-size: 17px;
    letter-spacing: 0.4px;
    text-transform: uppercase;
  }
  .person-title {
    font-size: 14px;
    margin-top: 2px;
  }
  .contact-list {
    list-style: none;
    position: absolute;
    left: 250px; top: 180px;
    font-size: 14px;
    line-height: 22px;
  }
  .contact-list li { display: flex; align-items: center; gap: 8px; }
  .contact-icon { width: 12px; height: 12px; flex: none; }
  .social-dot {
    width: 11px; height: 11px; flex: none;
    background: var(--paper); border-radius: 2px;
  }

  /* Logo side */
  .logo-side {
    display: flex; align-items: center; justify-content: center;
  }
  .logo-side .brand {
    display: flex; align-items: center; gap: 12px;
  }
  .logo-side .brand-mark { width: 14px; height: 14px; }
  .logo-side .brand-name { font-size: 40px; }
</style>
</head>
<body>

  <section class="card contact-side">
    <div class="floral-monogram" role="img" aria-label="Line-drawn floral illustration of roses and leaves wrapped around a large monogram letter"></div>

    <div class="brand">
      <span class="brand-mark"></span>
      <span class="brand-name">marlow ashby</span>
    </div>

    <div class="person">
      <p class="person-name">Elliot Hayes</p>
      <p class="person-title">Manager</p>
    </div>

    <ul class="contact-list">
      <li>
        <svg class="contact-icon" viewBox="0 0 24 24" aria-hidden="true"><path fill="#fff" d="M6.6 10.8a15.1 15.1 0 0 0 6.6 6.6l2.2-2.2c.3-.3.7-.4 1-.2 1.1.4 2.3.6 3.6.6.6 0 1 .4 1 1V20c0 .6-.4 1-1 1A17 17 0 0 1 3 4c0-.6.4-1 1-1h3.5c.6 0 1 .4 1 1 0 1.3.2 2.5.6 3.6.1.3 0 .7-.2 1z"/></svg>
        555-014-2100
      </li>
      <li>
        <svg class="contact-icon" viewBox="0 0 24 24" aria-hidden="true"><rect x="2" y="5" width="20" height="14" rx="1.5" fill="#fff"/><path d="M3 6l9 7 9-7" fill="none" stroke="#96325c" stroke-width="2"/></svg>
        hello@marlowashby.com
      </li>
      <li><span class="social-dot"></span>#marlowashby</li>
      <li><span class="social-dot"></span>#marlowashby</li>
    </ul>
  </section>

  <section class="card logo-side">
    <div class="brand">
      <span class="brand-mark"></span>
      <span class="brand-name">marlow ashby</span>
    </div>
  </section>

</body>
</html>
```